Business Card Design

We need a new business card design for a company based in Fernbrook, NM. We provide business consulting services in the information technology / services space. We like variations of the color blue, aqua, black, light tan, and white. Would like "cool" tones. The design should clearly communicate professionalism. Think outside the box - we don't want something "typical". Our company name is "Vantrell Advisory, LLC".
Updates

Thank you all for your submissions. We have seen some very creative and inspired designs. We have made a decision and will be moving forward with that design. Appreciate all of the hard work.

Industry/Entity Type

Information Technology

Contact Information for Business Card

Denise Harlow Trumbey
482 West Maple Ridge Dr.
Fernbrook, NM 76185

```html
<!DOCTYPE html>
<html lang="en">
<head>
<meta charset="utf-8">
<title>Vantrell Advisory — Business Card</title>
<link rel="stylesheet" href="https://fonts.googleapis.com/css2?family=Questrial&display=swap">
<style>
  :root {
    --backdrop: #2b2b2d;
    --card-white: #f2f2f2;
    --card-shade: #d9d9d9;
    --teal-bright: #1fb3c4;
    --teal-mid: #1796a6;
    --slate-deep: #2c3a40;
    --ink: #111416;
    --mark-white: #ffffff;
  }
  * { margin: 0; padding: 0; box-sizing: border-box; }
  html, body {
    width: 1200px;
    height: 900px;
    overflow: hidden;
    background: var(--backdrop);
  }
  .stage {
    width: 1200px;
    height: 900px;
    display: flex;
    align-items: center;
    justify-content: center;
  }
  .business-card {
    position: relative;
    width: 760px;
    height: 430px;
    background: linear-gradient(120deg, var(--card-white) 55%, var(--card-shade) 100%);
    overflow: hidden;
    font-family: "Questrial", sans-serif;
    box-shadow: 0 18px 40px rgba(0, 0, 0, 0.45);
  }
  .brand-panel {
    position: absolute;
    inset: 0;
    width: 100%;
    height: 100%;
  }
  .brand-lockup {
    position: absolute;
    left: 60px;
    top: 168px;
    display: flex;
    align-items: center;
    gap: 16px;
    color: var(--mark-white);
  }
  .brand-dot {
    width: 56px;
    height: 56px;
    border-radius: 50%;
    background: var(--mark-white);
    flex: none;
  }
  .brand-name {
    font-size: 28px;
    line-height: 1.15;
    color: var(--mark-white);
  }
  .contact-block {
    position: absolute;
    right: 56px;
    top: 160px;
    text-align: right;
    color: var(--ink);
  }
  .contact-name {
    font-size: 23px;
    font-weight: 400;
    letter-spacing: 0.4px;
    margin-bottom: 24px;
  }
  .contact-address {
    font-size: 13px;
    line-height: 1.45;
    letter-spacing: 0.3px;
  }
</style>
</head>
<body>
<main class="stage">
  <article class="business-card">
    <svg class="brand-panel" viewBox="0 0 760 430" preserveAspectRatio="none" aria-hidden="true">
      <defs>
        <linearGradient id="panelFill" x1="0" y1="0" x2="0" y2="1">
          <stop offset="0" stop-color="#1fb3c4"/>
          <stop offset="0.45" stop-color="#1796a6"/>
          <stop offset="1" stop-color="#2c3a40"/>
        </linearGradient>
        <linearGradient id="edgeGlow" x1="0" y1="0" x2="1" y2="0">
          <stop offset="0" stop-color="#ffffff" stop-opacity="0.9"/>
          <stop offset="1" stop-color="#ffffff" stop-opacity="0"/>
        </linearGradient>
      </defs>
      <polygon points="0,0 418,0 352,430 0,430" fill="url(#panelFill)"/>
      <polygon points="418,0 440,0 374,430 352,430" fill="url(#edgeGlow)"/>
    </svg>

    <div class="brand-lockup">
      <span class="brand-dot"></span>
      <span class="brand-name">Vantrell<br>Advisory</span>
    </div>

    <div class="contact-block">
      <h1 class="contact-name">Denise Harlow Trumbey</h1>
      <p class="contact-address">482 West Maple Ridge Dr. Fernbrook<br>NM 76185</p>
    </div>
  </article>
</main>
</body>
</html>
```